Verdant Solutions Business Card

want the back of card to be blue- with the logo in the center
front of card- info plus logo (info being mailing address, email address, and website address )
4 different names with titles to have on cards
1) Dalton Mirsky - Owner
2) Brenda Tolvin- Customer Relationship Specialist
3) Henri Kastner- Vice President of Sales
4) Wade Dunmor- Chief Technology Officer

Target Market(s)

tech company in the government/probation office industry

Industry/Entity Type

Government Office

Contact Information for Business Card

1) Dalton Mirsky - Owner

Colors
0355a3
ffffff

Requirements
Must have
• back side should be blue, with the logo placed in the center
• front side needs to include both the logo, as well as company info (info should include website address, email address, and mailing address)

```html
<!DOCTYPE html>
<html lang="en">
<head>
<meta charset="utf-8">
<title>Verdant Solutions Business Card</title>
<link rel="stylesheet" href="https://fonts.googleapis.com/css2?family=Roboto:wght@400;500;700&display=swap">
<style>
  :root {
    --navy: #172d57;
    --white: #ffffff;
    --ink: #1b1b1f;
    --ribbon: #808286;
    --ribbon-fold: #5d5f63;
    --stage: #6e7880;
  }
  * { box-sizing: border-box; margin: 0; padding: 0; }
  html, body { width: 1200px; height: 900px; overflow: hidden; }
  body {
    background: var(--stage);
    font-family: "Roboto", Arial, sans-serif;
    position: relative;
  }
  .card {
    position: absolute;
    width: 665px;
    height: 380px;
    border-radius: 22px;
    overflow: hidden;
    box-shadow: 0 10px 24px rgba(0,0,0,0.3);
  }
  .card-back {
    left: 268px; top: 50px;
    background: var(--navy);
    display: flex; align-items: center; justify-content: center;
  }
  .brand {
    display: flex; align-items: center; gap: 14px;
    font-weight: 500;
    letter-spacing: 0.04em;
    text-transform: uppercase;
    white-space: nowrap;
  }
  .brand-mark { display: block; border-radius: 50%; flex: none; }
  .card-back .brand { color: var(--white); font-size: 46px; }
  .card-back .brand-mark { width: 40px; height: 40px; background: var(--white); }

  .card-front { left: 268px; top: 470px; background: var(--white); }
  .front-panel {
    position: absolute; right: 0; top: 0;
    width: 300px; height: 100%;
    background: var(--navy);
    clip-path: polygon(0 0, 100% 0, 100% 100%, 26% 100%);
  }
  .card-front .brand {
    position: absolute; left: 48px; top: 128px;
    gap: 10px;
    color: var(--navy); font-size: 22px;
  }
  .card-front .brand-mark { width: 20px; height: 20px; background: var(--navy); }

  .name-ribbon {
    position: absolute; left: 350px; top: 44px;
    width: 240px; height: 56px;
    background: var(--ribbon);
    color: var(--white);
    text-align: center;
    padding-top: 9px;
  }
  .name-ribbon .person { font-size: 19px; font-weight: 700; }
  .name-ribbon .role { font-size: 11px; margin-top: 3px; }
  .ribbon-fold { position: absolute; left: 350px; top: 100px; }

  .contact-list {
    position: absolute; left: 48px; top: 230px;
    list-style: none;
    color: var(--ink); font-size: 17px;
  }
  .contact-list li { display: flex; align-items: center; gap: 14px; height: 30px; }
  .contact-icon {
    width: 22px; height: 22px; background: var(--navy);
    display: flex; align-items: center; justify-content: center;
  }

  .address {
    position: absolute; right: 36px; bottom: 90px;
    width: 210px;
    color: var(--white); font-size: 15px; line-height: 1.4;
    text-align: center;
  }
  .address svg { display: block; margin: 0 auto 8px; }
</style>
</head>
<body>

<section class="card card-back" aria-label="Card back">
  <div class="brand"><span class="brand-mark"></span>Verdant Solutions</div>
</section>

<section class="card card-front" aria-label="Card front">
  <div class="front-panel"></div>

  <div class="brand"><span class="brand-mark"></span>Verdant Solutions</div>

  <div class="name-ribbon">
    <div class="person">Dalton Mirsky</div>
    <div class="role">Owner</div>
  </div>
  <svg class="ribbon-fold" width="22" height="16" viewBox="0 0 22 16"><polygon points="0,0 22,0 22,16" fill="var(--ribbon-fold)"/></svg>

  <ul class="contact-list">
    <li><span class="contact-icon"><svg width="14" height="14" viewBox="0 0 24 24"><path fill="#fff" d="M6.6 10.8a15 15 0 0 0 6.6 6.6l2.2-2.2a1 1 0 0 1 1-.25 11.4 11.4 0 0 0 3.6.57 1 1 0 0 1 1 1V20a1 1 0 0 1-1 1A17 17 0 0 1 3 4a1 1 0 0 1 1-1h3.5a1 1 0 0 1 1 1c0 1.25.2 2.45.57 3.57a1 1 0 0 1-.25 1z"/></svg></span>123-456-1234</li>
    <li><span class="contact-icon"><svg width="14" height="14" viewBox="0 0 24 24"><rect x="4" y="8" width="16" height="12" rx="2" fill="#fff"/><rect x="7" y="3" width="10" height="7" fill="#fff"/><rect x="8" y="12" width="8" height="2" fill="var(--navy)"/></svg></span>111-222-1234</li>
    <li><span class="contact-icon"><svg width="14" height="14" viewBox="0 0 24 24"><rect x="2" y="5" width="20" height="14" fill="#fff"/><path d="M2 5l10 8 10-8" fill="none" stroke="var(--navy)" stroke-width="2"/></svg></span>yourmail@email.com</li>
    <li><span class="contact-icon"><svg width="14" height="14" viewBox="0 0 24 24"><circle cx="12" cy="12" r="9" fill="none" stroke="#fff" stroke-width="2"/><ellipse cx="12" cy="12" rx="4" ry="9" fill="none" stroke="#fff" stroke-width="1.6"/><path d="M3 12h18" stroke="#fff" stroke-width="1.6"/></svg></span>www.webaddress.com</li>
  </ul>

  <div class="address">
    <svg width="14" height="18" viewBox="0 0 24 32"><path fill="#fff" d="M12 0a11 11 0 0 0-11 11c0 8 11 21 11 21s11-13 11-21A11 11 0 0 0 12 0zm0 15a4 4 0 1 1 0-8 4 4 0 0 1 0 8z"/></svg>
    1234 Full address - Brookvale<br>New Jersey 12345
  </div>
</section>

</body>
</html>
```